Wordpress theme customised please - for new ecommerce homewares website

Hi, we need a wordpress theme customised for a business that will sell tea towels (aka kitchen towels/dish cloths).
We do not have a website currently, but wish to launch using wordpress + woocommerce + "the shopfront" theme (c/- plumkestrel).
BACKGROUND RE THE BUSINESS
Our products are very stylish and will appeal to people who like owning gorgeous things - people who love cooking and/or decorating their home beautifully, or maybe they like travelling and/or buying presents for themselves and friends/family etc.
As they are typically used in people's kitchens, so "fresh" and "clean" is important - however the site must look very upmarket: timeless yet current, and classic yet simple, but not pretty, fussy or edgy.
We believe we have a great opportunity to leverage the "feel" of the product - cotton & linen fabric that has real texture to it, is tactile, natural, raw, real... in the photos used on the website, the backgrounds etc
Our logo is attached - a very dark grey colour was chosen, with white stripes, so that its neutral colouring would coordinate well with our suppliers' existing packaging. (We will represent a number of brands.)
BACKGROUND RE THIS PROJECT
We already know we want to use "the shopfront" theme by plumkestrel, but we need help customising the look of this theme so it works well with our logo, looks really striking and doesn't look like everyone else's ie "straight out of the box".
It appears these are the types of things that can be changed:
LAYOUT:
home page design concept (eg with a cascade carousel)
page design concept for eg About Us, Contact Us, FAQs
landing page design concept
header; light footer; dark footer
COLOURS & BACKGROUNDS & BORDERS & SEPARATORS:
main theme colour; accent colour; primary font colour
header background; light footer background colour; dark footer background colour; copyright bar background colour
dark footer widget title border; dark footer list separators and borders; dark footer/copyright bar separator styles
FONTS:
main navigation text colour; secondary navigation text colour; dark footer text colour; copyright bar text colour
main font; secondary font
LASTLY
Please don't hesitate to ask questions, request further information etc This is the first time we've posted a design project like this so it's tricky to know what other information you will need, so please just get in touch, ok!
Thanks so much for your interest in this project, and best wishes.

```html
<!DOCTYPE html>
<html lang="en">
<head>
<meta charset="utf-8">
<title>Linen Drawer Co — Home</title>
<link rel="stylesheet" href="https://fonts.googleapis.com/css2?family=Cinzel:wght@400;700&family=Open+Sans:wght@400;600;700&family=Oswald:wght@300;400&family=Crimson+Text&display=swap">
<style>
:root{
  --ink:#2d3340;
  --slate:#545a6e;
  --slate-line:#8a90a3;
  --mist:#f1f2f6;
  --white:#ffffff;
  --gold:#f0b400;
  --muted:#c9ccd6;
  --grey-mark:#8f9196;
}
*{box-sizing:border-box;margin:0;padding:0}
html,body{width:712px;height:1200px;overflow:hidden}
body{position:relative;background:var(--ink);font-family:"Open Sans",sans-serif;color:var(--white)}
.abs{position:absolute}

/* top utility bar */
.utility-bar{left:0;top:0;width:712px;height:26px;background:var(--slate);font-size:7px;display:flex;align-items:center;justify-content:space-between;padding-left:17px;text-transform:uppercase}
.utility-links{display:flex;align-items:center;height:100%;gap:18px}
.utility-links .cart span{color:var(--gold)}
.search-btn{width:30px;height:100%;border-left:1px solid var(--ink);display:flex;align-items:center;justify-content:center}

/* brand + nav */
.brand-band{left:0;top:30px;width:712px;height:24px;border-top:2px solid var(--white);border-bottom:2px solid var(--white);display:flex;align-items:center;justify-content:center}
.brand-name{font-family:"Cinzel",serif;font-weight:700;font-size:19px;letter-spacing:.5px;color:var(--white)}
.main-nav{left:0;top:70px;width:712px;display:flex;justify-content:center;gap:18px;font-family:"Cinzel",serif;font-size:10px;letter-spacing:.4px}
.main-nav .dot{opacity:.8}

/* hero */
.hero{left:0;top:107px;width:712px;height:363px;background:linear-gradient(160deg,#cfd3d6 0%,#e6e8e8 45%,#d4d6d2 70%,#b9b7ae 100%)}

/* feature panel */
.feature-panel{left:13px;top:424px;width:682px;height:338px;background:var(--slate)}
.shipping-box{left:7px;top:7px;width:668px;height:76px;border:1px solid var(--white);text-align:center}
.shipping-title{font-family:"Cinzel",serif;font-size:15.5px;letter-spacing:.6px;margin-top:19px}
.shipping-rule{width:310px;height:1px;background:var(--slate-line);margin:6px auto 5px}
.shipping-sub{font-size:9px;color:var(--muted)}
.delivery-badge{left:556px;top:-7px;width:104px;height:104px;border-radius:50%;background:var(--ink);display:flex;flex-direction:column;align-items:center;justify-content:center;font-size:9.5px;line-height:13px;text-align:center}
.delivery-badge strong{font-size:12.5px;font-weight:700}

.section-title{font-family:"Oswald",sans-serif;font-weight:300;font-size:15px;text-transform:uppercase;letter-spacing:-.2px}
.featured-title{left:19px;top:104px}
.featured-rule{left:19px;top:126px;width:651px;height:1px;background:var(--slate-line)}
.carousel-arrows{left:626px;top:110px;display:flex;gap:6px}

.product{top:135px;width:137px}
.product-frame{width:137px;height:131px;background:var(--white);border:2px solid var(--white);outline:1px solid var(--slate-line);display:flex;align-items:center;justify-content:center}
.product-photo{width:100px;height:80px;border-radius:4px}
.product-cat{font-size:8px;font-weight:700;margin-top:12px}
.product-name{font-family:"Crimson Text",serif;font-size:9.5px;color:var(--muted);margin-top:1px}
.product-price{font-family:"Oswald",sans-serif;font-weight:300;font-size:17px;color:var(--muted);margin-top:2px;letter-spacing:-.5px}

/* partners */
.partners{left:0;top:770px;width:712px;height:196px;background:var(--mist);color:#4a4f5c}
.partners-title{left:21px;top:16px;color:#4a4f5c}
.partners-rule{left:21px;top:36px;width:663px;height:1px;background:#c7cad2}
.partner-arrow{top:92px;width:28px;height:27px;border:1px solid #9a9ea8;background:var(--white);display:flex;align-items:center;justify-content:center}
.partner-tile{top:58px;width:158px;height:104px;background:#eceef2;display:flex;align-items:center;justify-content:center}
.partner-badge{width:86px;height:86px;background:var(--grey-mark);opacity:.75}

/* footer */
.footer-heading{top:989px;font-size:8.5px;font-weight:700;text-transform:uppercase}
.footer-brand{left:10px;top:1008px;width:161px;height:20px;border-top:2px solid var(--white);border-bottom:2px solid var(--white);display:flex;align-items:center;justify-content:center;font-family:"Cinzel",serif;font-weight:700;font-size:12.5px}
.footer-about{left:11px;top:1036px;width:170px;font-size:8.5px;line-height:10.5px;color:#e6e8ee}
.tag-grid{left:192px;top:1013px;display:grid;grid-template-columns:repeat(3,47px);gap:4px 3px}
.tag{height:17px;border:1px solid var(--slate-line);font-size:8px;color:#d7dae2;display:flex;align-items:center;justify-content:center}
.info-links{left:366px;top:1019px;display:grid;grid-template-columns:80px 80px;row-gap:10px;font-size:8px;font-weight:700;text-transform:uppercase}
.social{left:540px;top:1017px;display:flex;gap:6px}
.social-dot{width:25px;height:25px;border-radius:50%;background:var(--white);color:var(--ink);font-size:11px;font-weight:700;display:flex;align-items:center;justify-content:center}

.copyright-bar{left:0;top:1148px;width:712px;height:52px;background:var(--slate);display:flex;align-items:center;justify-content:space-between;padding:0 18px 0 11px}
.pay-list{display:flex;gap:6px}
.pay-card{width:36px;height:22px;background:var(--white);color:var(--ink);border-radius:2px;font-size:6px;font-weight:700;display:flex;align-items:center;justify-content:center}
.copyright{font-size:8px;color:#e6e8ee}
</style>
</head>
<body>

<header>
  <div class="utility-bar abs">
    <span>Welcome to Linen Drawer Co</span>
    <div class="utility-links">
      <span>Shop</span>
      <span>Login</span>
      <span class="cart"><span>1 items</span> in cart</span>
      <span class="search-btn">
        <svg width="9" height="9" viewBox="0 0 10 10"><circle cx="4" cy="4" r="3" fill="none" stroke="#fff" stroke-width="1.6"/><line x1="6.3" y1="6.3" x2="9" y2="9" stroke="#fff" stroke-width="1.8"/></svg>
      </span>
    </div>
  </div>
  <div class="brand-band abs"><span class="brand-name">LINEN DRAWER CO</span></div>
  <nav class="main-nav abs">
    <span>HOME</span><span class="dot">·</span><span>ABOUT US</span><span class="dot">·</span><span>PRODUCTS</span><span class="dot">·</span><span>CONTACT US</span>
  </nav>
</header>

<div class="hero abs" role="img" aria-label="Kitchen bench scene with a folded blue tea towel, red coffee cup, boiled egg and a basket of lemons"></div>

<section class="feature-panel abs">
  <div class="shipping-box abs">
    <p class="shipping-title">FREE SHIPPING ON ALL ORDERS OVER $75</p>
    <div class="shipping-rule"></div>
    <p class="shipping-sub">NO REQUIREMENTS REQUIRED JUST SHOP ABOVE $75</p>
  </div>
  <div class="delivery-badge abs"><span>DELIVERED</span><span>TO YOU</span><span>DOOR</span><strong>IN 3 DAYS</strong></div>

  <h2 class="section-title featured-title abs">Featured Products</h2>
  <div class="carousel-arrows abs">
    <svg width="12" height="13" viewBox="0 0 12 13"><path d="M12 0V13L0 6.5Z" fill="#fff"/></svg>
    <svg width="12" height="13" viewBox="0 0 12 13"><path d="M0 0V13L12 6.5Z" fill="#fff"/></svg>
  </div>
  <div class="featured-rule abs"></div>

  <article class="product abs" style="left:19px">
    <div class="product-frame"><div class="product-photo" role="img" aria-label="Grey tea towel with pink and blue stripes" style="background:linear-gradient(135deg,#a9a59a,#c08cb0,#8fa0c4)"></div></div>
    <p class="product-cat">TOPS</p><p class="product-name">Ridge 89 Heritage Sweatshirt</p><p class="product-price">$101.23</p>
  </article>
  <article class="product abs" style="left:186px">
    <div class="product-frame"><div class="product-photo" role="img" aria-label="White tea towel with yellow stripes" style="background:linear-gradient(135deg,#f4d36a,#faf3dc,#f0c23c)"></div></div>
    <p class="product-cat">TOPS</p><p class="product-name">Ridge 89 Heritage Sweatshirt</p><p class="product-price">$101.23</p>
  </article>
  <article class="product abs" style="left:353px">
    <div class="product-frame"><div class="product-photo" role="img" aria-label="Stack of tea towels with red and blue borders tied with ribbon" style="background:linear-gradient(135deg,#d86b6b,#ece6dc,#5a74a8)"></div></div>
    <p class="product-cat">TOPS</p><p class="product-name">Ridge 89 Heritage Sweatshirt</p><p class="product-price">$101.23</p>
  </article>
  <article class="product abs" style="left:520px">
    <div class="product-frame"><div class="product-photo" role="img" aria-label="Blue and white checked tea towel" style="background:linear-gradient(135deg,#cdd6f0,#f4f6fc,#4a62b0)"></div></div>
    <p class="product-cat">TOPS</p><p class="product-name">Ridge 89 Heritage Sweatshirt</p><p class="product-price">$101.23</p>
  </article>
</section>

<section class="partners abs">
  <h2 class="section-title partners-title abs">Partners</h2>
  <div class="partners-rule abs"></div>
  <div class="partner-arrow abs" style="left:21px"><svg width="7" height="8" viewBox="0 0 7 8"><path d="M7 0V8L0 4Z" fill="#7a7e88"/></svg></div>
  <div class="partner-tile abs" style="left:72px"><div class="partner-badge" style="border-radius:4px"></div></div>
  <div class="partner-tile abs" style="left:270px"><div class="partner-badge" style="border-radius:50%"></div></div>
  <div class="partner-tile abs" style="left:468px"><div class="partner-badge" style="width:120px;height:60px;border-radius:4px"></div></div>
  <div class="partner-arrow abs" style="left:660px"><svg width="7" height="8" viewBox="0 0 7 8"><path d="M0 0V8L7 4Z" fill="#7a7e88"/></svg></div>
</section>

<footer>
  <h3 class="footer-heading abs" style="left:18px">About Linen Drawer Co</h3>
  <div class="footer-brand abs">LINEN DRAWER CO</div>
  <p class="footer-about abs">Lorem ipsum dolor sit amet, consectetur adipisicing elit, sed do eiusmod tempor incididunt ut labore et dolore magna aliqua. Ut enim ad minim veniam, quis nostrud exercitation ullamco laboris nisi ut aliquip ex ea commodo consequat.</p>

  <h3 class="footer-heading abs" style="left:192px">Tags</h3>
  <div class="tag-grid abs">
    <span class="tag">Catalog</span><span class="tag">Catalog</span><span class="tag">Catalog</span>
    <span class="tag">Catalog</span><span class="tag">Catalog</span><span class="tag">Catalog</span>
    <span class="tag">Catalog</span><span class="tag">Catalog</span><span class="tag">Catalog</span>
    <span class="tag">Catalog</span><span class="tag">Catalog</span><span class="tag">Catalog</span>
    <span class="tag">Catalog</span><span class="tag">Catalog</span><span class="tag">Catalog</span>
  </div>

  <h3 class="footer-heading abs" style="left:367px">Information</h3>
  <div class="info-links abs">
    <span>Track Orders</span><span>Blog</span>
    <span>FAQs</span><span>About Us</span>
    <span>Portfolio</span><span>Services</span>
    <span>Shop Sales</span><span>Contact Us</span>
  </div>

  <h3 class="footer-heading abs" style="left:541px">Connect with Linen Drawer Co</h3>
  <div class="social abs">
    <span class="social-dot" aria-label="Nook">N</span>
    <span class="social-dot" aria-label="Trellis">T</span>
    <span class="social-dot" aria-label="Wren">W</span>
    <span class="social-dot" aria-label="Pebble">P</span>
    <span class="social-dot" aria-label="Quay">Q</span>
  </div>

  <div class="copyright-bar abs">
    <div class="pay-list">
      <span class="pay-card">Vestra</span>
      <span class="pay-card">PayLoft</span>
      <span class="pay-card">Meridian</span>
      <span class="pay-card">Dovecard</span>
      <span class="pay-card">Arbormart</span>
    </div>
    <p class="copyright">© Copyright Linen Drawer Co 2013. All Rights Reserved</p>
  </div>
</footer>

</body>
</html>
```